Kestrel Lane flyer

Need a A6 size horizontal layout flyer. See attached example for ideas as well as some images I have which you can use. we are a hire car company that provides vehicles to clients who have recently been involved in car accidents and who's cars are currently getting fixed and so they lose the use of their own vehicle. see our website to keep flyer in line with website and for any further information kestrellane.com.au

Target Market(s)

people involved in not at fault car accidents

Industry/Entity Type

It Company

Requirements
Must have
• *ask people to let us know where they got our flyer from when they call us
• *call to action for people to call our phone number 1800 417 582
Should not have
• any mentioning that the vehicle is free

```html
<!DOCTYPE html>
<html lang="en">
<head>
<meta charset="utf-8">
<title>Kestrel Lane Flyer</title>
<link href="https://fonts.googleapis.com/css2?family=Montserrat:wght@500;600;700&display=swap" rel="stylesheet">
<style>
  :root {
    --orange: #ee8020;
    --blue: #1a73c2;
    --blue-soft: #5b87c8;
    --black: #0b0b0b;
    --white: #ffffff;
    --page: #ebebeb;
  }
  html, body {
    margin: 0;
    padding: 0;
    width: 999px;
    height: 1200px;
    overflow: hidden;
    background: var(--page);
    font-family: "Montserrat", Arial, sans-serif;
  }
  .flyer {
    position: absolute;
    left: 50px;
    top: 288px;
    width: 900px;
    height: 625px;
    background: var(--white);
    box-shadow: 0 18px 30px rgba(0,0,0,0.25);
    overflow: hidden;
  }
  .flyer-art {
    position: absolute;
    inset: 0;
    width: 900px;
    height: 625px;
  }
  .brand-name {
    position: absolute;
    left: 225px;
    top: 222px;
    width: 380px;
    text-align: center;
    color: var(--orange);
    font-weight: 700;
    font-size: 28px;
    margin: 0;
  }
  .headline {
    position: absolute;
    left: 24px;
    top: 292px;
    margin: 0;
    color: var(--blue);
    font-weight: 600;
    font-size: 22px;
    line-height: 29px;
  }
  .step-number {
    position: absolute;
    top: 404px;
    color: var(--white);
    font-weight: 600;
    font-size: 40px;
    line-height: 1;
  }
  .step-text {
    position: absolute;
    color: var(--white);
    font-weight: 500;
    font-size: 16px;
    line-height: 20px;
    margin: 0;
  }
  .feature {
    position: absolute;
    font-size: 16px;
    font-weight: 600;
    color: var(--black);
  }
  .ribbon-text {
    position: absolute;
    left: 510px;
    top: 517px;
    width: 335px;
    text-align: center;
    color: var(--orange);
    font-size: 13.5px;
    font-weight: 600;
    line-height: 17px;
    margin: 0;
  }
  .call-label {
    position: absolute;
    left: 30px;
    top: 556px;
    color: var(--white);
    font-size: 18px;
    font-weight: 600;
  }
  .phone-number {
    position: absolute;
    left: 76px;
    top: 579px;
    color: var(--white);
    font-size: 31px;
    font-weight: 600;
  }
  .free-call {
    position: absolute;
    left: 337px;
    top: 581px;
    color: var(--white);
    font-size: 28px;
    font-weight: 500;
  }
  .source-note {
    position: absolute;
    left: 596px;
    top: 575px;
    color: var(--white);
    font-size: 12.5px;
    font-weight: 500;
  }
  .website {
    position: absolute;
    left: 614px;
    top: 597px;
    color: var(--white);
    font-size: 16px;
    font-weight: 500;
  }
</style>
</head>
<body>
<main class="flyer">
  <svg class="flyer-art" viewBox="0 0 637 451" preserveAspectRatio="none" xmlns="http://www.w3.org/2000/svg">
    <defs>
      <linearGradient id="car-tones" x1="0" y1="0" x2="1" y2="1">
        <stop offset="0" stop-color="#3b3b3b"/>
        <stop offset="0.45" stop-color="#d9dde2"/>
        <stop offset="1" stop-color="#f4f5f7"/>
      </linearGradient>
      <linearGradient id="driver-tones" x1="0" y1="0" x2="1" y2="1">
        <stop offset="0" stop-color="#5d6773"/>
        <stop offset="0.5" stop-color="#e4e4e6"/>
        <stop offset="1" stop-color="#b83a3f"/>
      </linearGradient>
      <linearGradient id="couple-tones" x1="0" y1="0" x2="1" y2="1">
        <stop offset="0" stop-color="#c9ccd2"/>
        <stop offset="0.5" stop-color="#f1eeec"/>
        <stop offset="1" stop-color="#a8242c"/>
      </linearGradient>
    </defs>

    <polygon class="photo-car" role="img" aria-label="Photo of the front of a silver car" fill="url(#car-tones)"
      points="0,0 300,0 160,140 205,185 135,200 0,200"/>
    <polygon class="photo-driver" role="img" aria-label="Photo of a smiling couple seated in a car" fill="url(#driver-tones)"
      points="300,0 570,0 520,75 430,140"/>
    <polygon class="photo-couple" role="img" aria-label="Photo of a couple receiving keys to a red car" fill="url(#couple-tones)"
      points="520,80 637,195 637,284 400,284"/>

    <polygon class="accent-orange" fill="var(--orange)" points="0,62 0,200 135,200"/>
    <polygon class="accent-blue" fill="var(--blue-soft)" points="572,0 637,0 637,152 522,76"/>
    <polyline fill="none" stroke="var(--orange)" stroke-width="3" points="430,140 575,0"/>
    <polyline fill="none" stroke="var(--blue)" stroke-width="3" points="400,283 520,80 637,196"/>
    <polyline fill="none" stroke="var(--blue)" stroke-width="3" points="300,0 430,130"/>
    <polyline fill="none" stroke="var(--blue)" stroke-width="3" points="0,45 160,142"/>

    <polygon class="brand-diamond" fill="var(--black)" stroke="var(--blue)" stroke-width="3"
      points="294,6 428,142 294,280 158,142"/>
    <circle cx="294" cy="128" r="11" fill="var(--blue)"/>

    <rect x="17" y="287" width="591" height="75" fill="var(--orange)"/>
    <polyline fill="none" stroke="var(--white)" stroke-width="6" points="176,287 190,324 176,362"/>
    <polyline fill="none" stroke="var(--blue)" stroke-width="2.5" points="180,287 194,324 180,362"/>
    <polyline fill="none" stroke="var(--white)" stroke-width="6" points="360,287 374,324 360,362"/>
    <polyline fill="none" stroke="var(--blue)" stroke-width="2.5" points="364,287 378,324 364,362"/>

    <g fill="none" stroke="var(--white)" stroke-width="1.5">
      <circle cx="96" cy="306" r="8"/>
      <path d="M90 313 l-4 6 l8 -3"/>
      <path d="M92 303 q0 5 6 6"/>
      <rect x="266" y="297" width="12" height="17" rx="1"/>
      <path d="M269 302 h6 M269 306 h6 M269 310 h3"/>
      <path d="M276 314 l6 -8"/>
      <path d="M456 307 h30 q4 0 4 4 v4 h-38 v-4 q0 -4 4 -4z"/>
      <path d="M460 307 l5 -6 h13 l6 6"/>
      <circle cx="460" cy="315" r="3"/>
      <circle cx="482" cy="315" r="3"/>
    </g>

    <g fill="var(--orange)">
      <polygon points="20,374 30,377 20,380"/>
      <polygon points="193,374 203,377 193,380"/>
      <polygon points="124,393 134,396 124,399"/>
    </g>

    <polygon class="ribbon" fill="var(--black)" points="356,369 603,369 593,386 603,403 356,403 366,386"/>

    <rect x="0" y="411" width="637" height="40" fill="var(--blue)"/>
    <polygon fill="var(--blue)" points="0,401 106,401 116,411 0,411"/>
    <circle cx="31" cy="431" r="6" fill="none" stroke="var(--white)" stroke-width="1.3"/>
    <path d="M28.5 428 q0 5 5 6" fill="none" stroke="var(--white)" stroke-width="1.5"/>
    <circle cx="427" cy="437" r="4" fill="none" stroke="var(--white)" stroke-width="1"/>
    <path d="M423 437 h8 M427 433 q-2 4 0 8 q2 -4 0 -8" fill="none" stroke="var(--white)" stroke-width="0.8"/>
  </svg>

  <p class="brand-name">Kestrel Lane</p>

  <h1 class="headline">Arranging An Accident<br>Replacement Vehicle For<br>Yourself Is Easy As 1,2,3</h1>

  <span class="step-number" style="left:76px;">1</span>
  <p class="step-text" style="left:53px; top:447px;">Apply online or call<br>1800 417 582</p>

  <span class="step-number" style="left:318px;">2</span>
  <p class="step-text" style="left:288px; top:462px;">Provide accident details</p>

  <span class="step-number" style="left:591px;">3</span>
  <p class="step-text" style="left:556px; top:447px;">You get a replacement vehicle<br>We take care of the rest</p>

  <span class="feature" style="left:50px; top:512px;">Free Delivery</span>
  <span class="feature" style="left:294px; top:512px;">Late Model</span>
  <span class="feature" style="left:196px; top:538px;">New Vehicles</span>

  <p class="ribbon-text">AUSTRALIA'S NO.1 CAR ACCIDENT<br>REPLACEMENT SERVICE</p>

  <span class="call-label">Call us on</span>
  <span class="phone-number">1800-417-582</span>
  <span class="free-call">FREE CALL</span>
  <span class="source-note">Please tell us where you got this flyer</span>
  <span class="website">www.kestrellane.com.au</span>
</main>
</body>
</html>
```